Marbrook Jewelers New Website Design

This project is to provide a new design for an existing website. The existing website is marbrookjewelers dot com . I have created a overview document that outlines all the details for the project. I do not need the design to be converted into HTML. I have a team for that already so please don't ask. I have a lot of images .. too many to upload here so they are on my dev server located at pinfernstudio com slash marbrook slash assets

Number of Pages Required

1 page

```html
<!DOCTYPE html>
<html lang="en">
<head>
<meta charset="utf-8">
<title>Marbrook Jewelers</title>
<link href="https://fonts.googleapis.com/css2?family=Quattrocento:wght@400;700&family=Josefin+Sans:wght@300;400;600;700&display=swap" rel="stylesheet">
<style>
:root{
  --bg:#f5f3ed;
  --band:#ebe9e1;
  --bar:#efece5;
  --ink:#262626;
  --text:#4a4744;
  --rose:#c0847a;
  --gold:#d7b24a;
  --line:#dcd8cf;
  --white:#ffffff;
  --dark:#262626;
}
*{margin:0;padding:0;box-sizing:border-box}
html,body{width:1200px;height:4580px;overflow:hidden}
body{background:var(--bg);font-family:'Josefin Sans',sans-serif;color:var(--text);position:relative}
.abs{position:absolute}
.serif{font-family:'Quattrocento',serif}
.rose{color:var(--rose)}
h1,h2{font-family:'Quattrocento',serif;font-weight:700;color:var(--ink);line-height:1}
.topbar{left:0;top:0;width:1200px;height:36px;background:var(--bar);font-size:13px;letter-spacing:1px;color:#6b6761}
.topbar span{position:absolute;top:12px;display:flex;align-items:center;gap:8px}
.nav{top:74px;right:100px;display:flex;gap:34px;font-size:12.5px;letter-spacing:1px;color:#3a3836;text-transform:uppercase}
.eyebrow{font-size:11px;letter-spacing:1px;color:var(--gold);text-transform:uppercase}
.para{font-size:15px;line-height:30px;color:var(--text)}
.btn-outline{border:2px solid var(--ink);font-size:12px;font-weight:700;letter-spacing:.5px;color:var(--ink);display:flex;align-items:center;justify-content:center;text-transform:uppercase}
.btn-dark{background:var(--dark);color:#fff;font-size:12px;font-weight:700;letter-spacing:.5px;display:flex;align-items:center;justify-content:center;text-transform:uppercase}
.photo{position:absolute}
.script{position:absolute;background:linear-gradient(90deg,rgba(215,178,74,0),rgba(215,178,74,.22),rgba(215,178,74,0))}
.rule{position:absolute;left:85px;width:1028px;height:1px;background:var(--line)}
.rule::before,.rule::after{content:"";position:absolute;top:-5px;width:9px;height:9px;border:1px solid var(--line);border-radius:50%;background:var(--bg)}
.rule::before{left:-9px}.rule::after{right:-9px}
.ghost{font-family:'Quattrocento',serif;font-weight:700;font-size:110px;letter-spacing:4px;color:rgba(0,0,0,.025);white-space:nowrap}
.card{position:absolute;width:270px;height:333px;background:var(--white);display:flex;align-items:center;justify-content:center}
.card .ring{width:170px;height:120px;border-radius:50%}
.links{font-size:13px;letter-spacing:2px;display:flex;gap:18px;align-items:center;color:var(--ink)}
.links a{color:inherit;text-decoration:underline;text-underline-offset:4px}
.dot{width:6px;height:6px;border-radius:50%;background:var(--ink)}
.foot-h{font-size:16px;letter-spacing:1px;color:var(--rose)}
.foot-list{list-style:none;font-size:14px;letter-spacing:1px;line-height:28.4px;color:#3a3836}
</style>
</head>
<body>

<div class="abs topbar">
  <span style="left:100px"><svg width="10" height="13" viewBox="0 0 10 13"><path d="M5 0a5 5 0 0 0-5 5c0 4 5 8 5 8s5-4 5-8a5 5 0 0 0-5-5zm0 7a2 2 0 1 1 0-4 2 2 0 0 1 0 4z" fill="#c0847a"/></svg>48 Alder Row, Fenwick, MN</span>
  <span style="left:375px"><svg width="11" height="11" viewBox="0 0 12 12"><path d="M2.5 0l2 3-1.2 1.3a7 7 0 0 0 4.4 4.4L9 7.5l3 2-1.5 2.5C5 12 0 7 0 1.5z" fill="#c0847a"/></svg>555-201-4470</span>
  <span style="left:535px"><svg width="11" height="11" viewBox="0 0 12 12"><path d="M2.5 0l2 3-1.2 1.3a7 7 0 0 0 4.4 4.4L9 7.5l3 2-1.5 2.5C5 12 0 7 0 1.5z" fill="#c0847a"/></svg>555-308-1192</span>
  <span style="left:1046px;font-size:11px">▾EN <svg width="14" height="14" viewBox="0 0 14 14" fill="none" stroke="#c0847a"><circle cx="7" cy="7" r="6"/><path d="M1 7h12M7 1c3 3 3 9 0 12M7 1c-3 3-3 9 0 12"/></svg></span>
</div>

<nav class="abs nav">
  <span>Custom Jewelry ▾</span><span>Gallery</span><span>Jewelery Repair</span><span>Gift Ideas</span><span>Engraving &amp; Trophies</span>
</nav>

<!-- Hero -->
<div class="abs eyebrow" style="left:100px;top:200px;display:flex;align-items:center;gap:6px">Welcome to Marbrook Jewelers <i style="display:inline-block;width:160px;height:1px;background:var(--gold)"></i></div>
<h1 class="abs" style="left:100px;top:246px;font-size:48px;line-height:78px">Modular <span class="rose">Jewelry</span><br>For Every Mood.</h1>
<p class="abs para" style="left:100px;top:407px;width:400px">Lorem ipsum dolor sit amet, consectetur adipiscing elit. Donec tristique ac est at posuere. Morbi egestas turpis vitae nibh sodales scelerisque.</p>
<div class="abs btn-outline" style="left:100px;top:517px;width:210px;height:47px">Discover Catalogue</div>

<div class="photo" role="img" aria-label="Pearl ring on black background" style="left:558px;top:174px;width:110px;height:406px;background:linear-gradient(160deg,#1a1a1a,#050505 60%,#2a2a2a)"></div>
<div class="photo" role="img" aria-label="Woman wearing a fine gold necklace and white shirt" style="left:683px;top:149px;width:291px;height:454px;background:linear-gradient(160deg,#cbbfb3,#a99686 55%,#e6e1dc)"></div>
<div class="abs" style="left:688px;top:154px;width:40px;height:38px;background:#2b2b2b;color:#fff;font-family:'Josefin Sans',sans-serif;font-size:20px;display:flex;align-items:center;justify-content:center">01</div>
<div class="photo" role="img" aria-label="Black and white hand wearing a ring" style="left:987px;top:174px;width:113px;height:404px;background:linear-gradient(160deg,#d8d8d8,#9a9a9a 55%,#e8e8e8)"></div>
<div class="script" role="img" aria-label="Hand lettered script: Elegance Lasts Longer Than Life" style="left:160px;top:570px;width:570px;height:123px"></div>
<svg class="abs" style="left:995px;top:620px" width="108" height="16" viewBox="0 0 108 16" fill="none" stroke="#2b2b2b" stroke-width="1.3"><path d="M28 8H2M8 2L2 8l6 6" stroke="#999"/><path d="M44 8h62M100 2l6 6-6 6"/></svg>
<div class="rule" style="top:706px"></div>

<!-- Welcome -->
<div class="abs ghost" style="left:240px;top:800px">FASHIONABLE</div>
<div class="abs ghost" style="left:110px;top:1315px">FASHIONABLE</div>
<div class="photo" role="img" aria-label="Jewelry store front window at night with lit display cases" style="left:100px;top:875px;width:645px;height:442px;background:linear-gradient(180deg,#2a2420 0%,#6b5540 30%,#3a3530 55%,#1e2630 100%)"></div>
<h2 class="abs" style="left:740px;top:892px;font-size:48px;line-height:69px">Welcome To <span class="rose">The</span><br><span class="rose">Marbrook</span> Store</h2>
<div class="abs" style="left:677px;top:1063px;width:395px;height:338px;border:4px solid #fff;background:var(--bg)"></div>
<p class="abs" style="left:697px;top:1100px;width:355px;font-size:15px;line-height:30px;text-align:center;color:var(--text)">Marbrook Jewelers is an independent, family owned jewelry store located in the heart of Downtown Fenwick. Owner, Daniel Marbrook has been with the business since 1990. His wife, Helen, joined the business in 2010, store manager, Tom, came on board in 2016 and Lucia joined the team in 2021. Marbrook Jewelers specializes in engagement rings, fashion jewelry and custom designed pieces.</p>
<div class="abs btn-dark" style="left:965px;top:1387px;width:134px;height:41px">Read More</div>
<div class="script" role="img" aria-label="Hand lettered script: Artistry in Gold &amp; Silver" style="left:250px;top:1298px;width:460px;height:169px"></div>

<!-- Gallery -->
<section class="abs" style="left:0;top:1579px;width:1200px;height:1145px;background:var(--band);overflow:hidden">
  <svg class="abs" style="left:0;top:0" width="1200" height="1145" fill="none" stroke="#fff" stroke-width="1.5"><path d="M0 55C250 40 700 80 1000 260S1150 480 1200 560"/><path d="M0 390C120 470 190 560 260 700"/><path d="M700 1145C900 960 1050 880 1200 860"/></svg>
  <div class="abs" role="img" aria-label="Gold filigree ornament" style="left:545px;top:40px;width:110px;height:30px;background:linear-gradient(90deg,rgba(215,178,74,.2),rgba(215,178,74,.55),rgba(215,178,74,.2));border-radius:15px"></div>
  <h2 class="abs" style="left:0;width:1200px;top:108px;text-align:center;font-size:48px">Every Piece <span class="rose">Tells a Story</span></h2>
  <div class="abs" role="img" aria-label="Grey line ornament" style="left:1005px;top:158px;width:110px;height:105px;background:linear-gradient(135deg,rgba(150,150,150,.25),rgba(150,150,150,0))"></div>
  <div class="abs" role="img" aria-label="Grey line ornament" style="left:85px;top:905px;width:110px;height:105px;background:linear-gradient(315deg,rgba(150,150,150,.25),rgba(150,150,150,0))"></div>
</section>
<div class="card" style="left:169px;top:1817px"><div class="ring" role="img" aria-label="Silver infinity knot diamond ring" style="background:radial-gradient(ellipse,#fff 35%,#e6e2ec 50%,#fff 70%)"></div></div>
<div class="card" style="left:464px;top:1817px"><div class="ring" role="img" aria-label="White gold crossover diamond ring" style="background:radial-gradient(ellipse,#fff 35%,#e1dfe6 50%,#fff 70%)"></div></div>
<div class="card" style="left:761px;top:1817px"><div class="ring" role="img" aria-label="Rose gold interlocking circles ring" style="background:radial-gradient(ellipse,#fff 30%,#e8c7a8 50%,#fff 70%)"></div></div>
<div class="card" style="left:169px;top:2174px"><div class="ring" role="img" aria-label="Rose gold multi band ring with diamond flower" style="background:radial-gradient(ellipse,#fff 25%,#e7b8a6 50%,#fff 70%)"></div></div>
<div class="card" style="left:464px;top:2174px"><div class="ring" role="img" aria-label="Silver and gold multi band ring" style="background:radial-gradient(ellipse,#fff 25%,#ddd4c2 50%,#fff 70%)"></div></div>
<div class="card" style="left:761px;top:2174px"><div class="ring" role="img" aria-label="Gold multi band ring with diamond squares" style="background:radial-gradient(ellipse,#fff 25%,#e6c58c 50%,#fff 70%)"></div></div>
<div class="abs btn-dark" style="left:450px;top:2574px;width:299px;height:48px">See Full Gallery</div>

<!-- Social -->
<h2 class="abs" style="left:0;width:1200px;top:2836px;text-align:center;font-size:48px">We Are On <span class="rose">Sharebook</span></h2>
<div class="script" role="img" aria-label="Hand lettered script: Give Us a Visit" style="left:450px;top:2910px;width:300px;height:120px"></div>
<div class="photo" role="img" aria-label="Woman in white shirt wearing a pendant" style="left:101px;top:3074px;width:233px;height:233px;background:linear-gradient(160deg,#d9cdc2,#b19c8c 50%,#efeae6)"></div>
<div class="photo" role="img" aria-label="Hands with rings on beige satin dress" style="left:356px;top:3074px;width:233px;height:233px;background:linear-gradient(160deg,#6a5a48,#c8ac86 50%,#e2d2b6)"></div>
<div class="photo" role="img" aria-label="Hands with rings over blue jeans" style="left:610px;top:3074px;width:233px;height:233px;background:linear-gradient(160deg,#4f4a3c,#8d8a78 45%,#b8c4d4)"></div>
<div class="photo" role="img" aria-label="Woman in pink top wearing necklace" style="left:864px;top:3074px;width:233px;height:233px;background:linear-gradient(160deg,#f2ece8,#d7a896 55%,#f4e9e4)"></div>
<div class="abs links" style="left:0;width:1200px;top:3350px;justify-content:center"><a>Sharebook</a><i class="dot"></i><a>Snapgrid</a><i class="dot"></i><a>Pinspire</a></div>

<!-- Elegant -->
<section class="abs" style="left:0;top:3476px;width:1200px;height:650px;background:var(--band)"></section>
<h2 class="abs" style="left:100px;top:3620px;font-size:48px;line-height:78px">Elegant <span class="rose">Minimal</span><br><span class="rose">Designs</span> at Marbrook</h2>
<p class="abs para" style="left:100px;top:3783px;width:470px">Lorem ipsum dolor sit amet, consectetur adipiscing elit. Donec tristique ac est at posuere. Morbi egestas turpis vitae nibh sodales scelerisque.</p>
<div class="abs btn-outline" style="left:100px;top:3896px;width:210px;height:46px">Discover Catalogue</div>
<p class="abs" style="left:100px;top:3970px;font-size:11px;font-weight:700;line-height:18px;color:var(--ink);text-transform:uppercase">Our store is open Monday to<br>Friday - from 8am to 10pm</p>
<div class="photo" role="img" aria-label="Hand touching gold necklace against blue denim" style="left:624px;top:3538px;width:475px;height:418px;background:linear-gradient(160deg,#8e99b4,#b69a86 50%,#6f7c9c)"></div>
<div class="photo" role="img" aria-label="Gold earring resting on open book" style="left:402px;top:3908px;width:325px;height:176px;background:linear-gradient(120deg,#b58a5a,#e8dcc4 50%,#8a6a48)"></div>
<div class="script" role="img" aria-label="Hand lettered script: 30 Years at Your Service" style="left:520px;top:3950px;width:570px;height:150px"></div>
<div class="rule" style="top:4126px;background:#d8d4cb"></div>

<!-- Footer -->
<p class="abs" style="left:100px;top:4273px;width:450px;font-size:13.5px;line-height:27px;color:var(--text)">Lorem ipsum dolor sit amet, consectetur adipiscing elit. Aenean feugiat et arcu sed ullamcorper. Mauris nec lacus sed purus pharetra maximus. Sed vitae porta justo, vel dignissim nisi.</p>
<div class="abs foot-h" style="left:100px;top:4386px">Join Our Newsletter</div>
<div class="abs" style="left:100px;top:4422px;width:305px;height:36px;background:#fff;font-size:10px;color:#aaa;padding:13px 0 0 12px">Enter Your Email Adress</div>
<div class="abs" style="left:405px;top:4422px;width:36px;height:36px;background:var(--dark);display:flex;align-items:center;justify-content:center"><svg width="18" height="10" viewBox="0 0 18 10" fill="none" stroke="#fff" stroke-width="1.5"><path d="M0 5h16M12 1l4 4-4 4"/></svg></div>

<div class="abs foot-h" style="left:613px;top:4206px">Navigation</div>
<ul class="abs foot-list" style="left:613px;top:4238px"><li>Company</li><li>Custom Jewelry</li><li>Jewelry Repairs</li><li>Showcase</li><li>Resources</li><li>Gallery</li><li>Engraving &amp; Trophies</li><li>Gifts Ideas</li></ul>

<div class="abs foot-h" style="left:857px;top:4206px">Contact</div>
<ul class="abs foot-list" style="left:857px;top:4238px"><li>48 Alder Row, Fenwick, MN</li><li>555-201-4470</li><li>555-308-1192</li></ul>
<div class="abs foot-h" style="left:857px;top:4343px">Find Us On Social Media</div>
<div class="abs" style="left:857px;top:4382px;font-size:12px;letter-spacing:1px;color:#3a3836;text-transform:uppercase">Snapgrid &nbsp;•&nbsp; Sharebook</div>

<div class="abs" style="left:100px;top:4535px;font-size:13.5px;letter-spacing:1px;color:#3a3836">©2022 Marbrook Jewelers: Northland Jeweler. All Rights Reserved.</div>
<div class="abs" style="right:100px;top:4535px;font-size:13.5px;letter-spacing:1px;color:var(--rose)">Privacy Policies &nbsp;•&nbsp; Terms &amp; Conditions</div>

</body>
</html>
```